DL Flyer for garden consultants. I will supply text and logo

To design an eye catching but simple, uncluttered flyer for letter box distribution. The text and logo are provided.

```html
<!DOCTYPE html>
<html lang="en">
<head>
<meta charset="utf-8">
<title>Fernley Garden Advisors – DL Flyer</title>
<link href="https://fonts.googleapis.com/css2?family=Roboto:wght@300;400&display=swap" rel="stylesheet">
<style>
  :root {
    --stage: #000000;
    --label: #9a9a9a;
    --paper: #ffffff;
    --white: #ffffff;
    --green-dark: #1d6b36;
    --green-light: #8cc63f;
    --green-band: #7ab540;
    --rule: #c5e09a;
    --photo-top: #5a8ccb;
    --photo-bottom: #9dbbe0;
  }
  * { margin: 0; padding: 0; box-sizing: border-box; }
  html, body {
    width: 1200px; height: 854px; overflow: hidden;
    background: var(--stage);
    font-family: "Roboto", Arial, sans-serif;
  }
  .stage { position: relative; width: 1200px; height: 854px; }
  .side-label {
    position: absolute; top: 14px; width: 528px; text-align: center;
    color: var(--label); font-size: 15px; font-weight: 400; letter-spacing: 0.5px;
  }
  .panel { position: absolute; top: 44px; width: 528px; height: 768px; overflow: hidden; }
  .panel--front { left: 40px; }
  .panel--back { left: 636px; background: var(--paper); }
  .side-label--front { left: 40px; }
  .side-label--back { left: 636px; }

  .cover-photo {
    position: absolute; inset: 0;
    background: linear-gradient(to bottom, var(--photo-top), var(--photo-bottom));
  }
  .front-question {
    position: absolute; left: 64px; top: 134px;
    color: var(--white); font-weight: 300; font-size: 34px; line-height: 42px;
  }
  .front-well {
    position: absolute; right: 88px; top: 230px;
    color: var(--white); font-weight: 300; font-size: 34px; letter-spacing: 1px;
  }
  .front-url {
    position: absolute; left: 0; right: 0; top: 708px; text-align: center;
    color: var(--white); font-weight: 300; font-size: 21px;
  }

  .brand {
    position: absolute; left: 64px; top: 84px;
    display: flex; align-items: center; gap: 18px;
    color: var(--green-light); font-weight: 400;
  }
  .brand-square { width: 86px; height: 86px; background: var(--green-light); }
  .brand-name { font-size: 58px; line-height: 60px; }
  .brand-sub { font-size: 19px; letter-spacing: 4px; margin-top: 6px; }

  .tagline {
    position: absolute; left: 74px; top: 296px;
    color: var(--green-dark); font-size: 32px; font-weight: 400;
  }
  .services { position: absolute; left: 74px; top: 368px; width: 384px; list-style: none; }
  .service { margin-bottom: 30px; }
  .service:nth-child(2) { margin-bottom: 50px; }
  .service-title {
    display: flex; align-items: center; gap: 6px;
    color: var(--green-dark); font-size: 18px; white-space: nowrap;
    padding-bottom: 9px; border-bottom: 1px solid var(--rule);
  }
  .service-bullet { width: 11px; height: 11px; background: var(--green-light); flex: none; }
  .service-note {
    color: var(--green-light); font-size: 16.5px; line-height: 22px;
    padding: 4px 0 0 15px;
  }
  .url-band {
    position: absolute; left: 0; right: 0; top: 706px; height: 34px;
    background: var(--green-band);
    color: var(--white); font-size: 21px; font-weight: 300;
    display: flex; align-items: center; justify-content: center;
  }
</style>
</head>
<body>
<div class="stage">
  <div class="side-label side-label--front">SIDE - 1</div>
  <div class="side-label side-label--back">SIDE - 2</div>

  <section class="panel panel--front">
    <div class="cover-photo" role="img" aria-label="Photograph of a wide field of colourful tulips under a blue, lightly clouded sky"></div>
    <p class="front-question">Have you been thinking<br>about your garden lately?</p>
    <p class="front-well">Well………</p>
    <p class="front-url">www.fernleygardenadvisors.com.au</p>
  </section>

  <section class="panel panel--back">
    <div class="brand">
      <div class="brand-square"></div>
      <div>
        <div class="brand-name">Fernley</div>
        <div class="brand-sub">GARDEN ADVISORS</div>
      </div>
    </div>

    <p class="tagline">.....we can help.</p>

    <ul class="services">
      <li class="service">
        <div class="service-title"><span class="service-bullet"></span>Garden Assessment Consultation and Report</div>
        <p class="service-note">...... information vital to ensuring your dream becomes reality!</p>
      </li>
      <li class="service">
        <div class="service-title"><span class="service-bullet"></span>Pre Sale Consultation and Report</div>
        <p class="service-note">….. maximise your sale dollar!</p>
      </li>
      <li class="service">
        <div class="service-title"><span class="service-bullet"></span>Develop a Plant Portfolio</div>
        <p class="service-note">….. successfully navigate the plant maze!</p>
      </li>
    </ul>

    <div class="url-band">www.fernleygardenadvisors.com.au</div>
  </section>
</div>
</body>
</html>
```